Product Page

We're marketing an on line educational product, and need a savvy designer to fix a web page that lacks pazazz. We're looking for a designer who can take a lot of information and present it neatly and elegantly, and put all the relevant testimonials in there without loosing cool factor. Right now we need just one page designed, but the winner will have the chance to re-do the entire site, with lots more content coming down the line that will need the new look.

The current page is here: www.plorvetune.com/sign-up. This should be combined with the attached PDF that has a lot more text information.

Note: The previous file listed as a pdf was a jpg. Sorry about that! Now there's a real pdf available for you to download.

I have added a jpg of myself. If you can use that I would appreciate it. I've also uploaded an example of a pricing page. Let me know how you would charge for this extra page.

Target Market(s)

Men and women in their forties who want to improve their singing but have other careers and are looking for high quality voice instruction.

The page must have an attractive "Get Started" button prominently displayed.

Industry/Entity Type

Marketing

Requirements
Must have
• Above the fold: clear buy now button, some testimonials, and the video. Should have a background that makes reading the text easy-not black. The new page must work somehow with the existing theme, although we will be re-designing the whole site soon with your help.
Nice to have
• Some navigation to organize a lot of text

```html
<!DOCTYPE html>
<html lang="en">
<head>
<meta charset="utf-8">
<title>AdrianKell School of Voice</title>
<link href="https://fonts.googleapis.com/css2?family=Oswald:wght@300;400;500&family=Open+Sans:wght@400&display=swap" rel="stylesheet">
<style>
  :root {
    --brand-blue: #29a8e0;
    --brand-navy: #3b5998;
    --ink: #2a2a2a;
    --body-grey: #5a5a5a;
    --hero-light: #ececec;
    --hero-mid: #d9d9d9;
    --divider: #c8c8c8;
    --footer-bg: #000000;
    --white: #ffffff;
  }
  * { box-sizing: border-box; margin: 0; padding: 0; }
  html, body { width: 1200px; height: 1072px; overflow: hidden; background: var(--white); }
  body { position: relative; font-family: Arial, Helvetica, sans-serif; }

  .hero {
    position: absolute; left: 0; top: 0; width: 1200px; height: 534px;
    background: radial-gradient(ellipse at 60% 40%, var(--hero-light), var(--hero-mid));
    overflow: hidden;
  }
  .hero-portrait {
    position: absolute; left: 0; top: 0; width: 450px; height: 534px;
    background: linear-gradient(160deg, #3a3a3a 0%, #151515 55%, #050505 100%);
    clip-path: polygon(70px 0, 290px 0, 305px 110px, 290px 210px, 320px 300px, 345px 400px, 450px 534px, 0 534px, 0 300px, 55px 230px, 75px 120px);
  }
  .brand {
    position: absolute; display: flex; align-items: center; gap: 14px;
    font-family: "Open Sans", Arial, sans-serif; font-weight: 400; line-height: 1.1;
  }
  .brand-dot { width: 44px; height: 44px; border-radius: 50%; background: var(--brand-blue); flex: none; }
  .brand-name { color: var(--ink); font-size: 34px; }
  .brand-name small { display: block; font-size: 22px; padding-left: 28px; }
  .hero .brand { left: 342px; top: 30px; }
  .footer .brand { left: 50px; top: 40px; }
  .footer .brand-name { color: var(--white); }

  .social { position: absolute; display: flex; gap: 15px; }
  .social span { width: 49px; height: 49px; border-radius: 50%; display: block; }
  .social .s-one { background: var(--brand-blue); }
  .social .s-two { background: var(--brand-navy); }
  .hero .social { left: 1008px; top: 43px; }
  .footer .social { left: 1008px; top: 56px; }

  .main-nav { position: absolute; left: 374px; top: 158px; list-style: none; }
  .main-nav li {
    font-family: Oswald, "Arial Narrow", sans-serif; font-weight: 500; font-size: 31px;
    line-height: 42px; color: var(--ink); text-transform: uppercase; letter-spacing: -0.3px;
  }
  .main-nav li.is-active { color: var(--brand-blue); }

  .video { position: absolute; left: 714px; top: 129px; width: 420px; height: 273px; background: #111; }
  .video-frame { width: 420px; height: 237px; background: linear-gradient(180deg, #4a4a4a, #262626); }
  .video-controls { display: flex; align-items: center; gap: 8px; height: 36px; padding: 0 10px; background: #1b1b1b; }
  .video-controls .play { width: 10px; height: 12px; border-left: 3px solid var(--brand-blue); border-right: 3px solid var(--brand-blue); }
  .video-controls .time { color: #888; font-size: 8px; }
  .video-controls .track { flex: 1; height: 18px; background: #3a3a3a; position: relative; }
  .video-controls .track::before { content: ""; position: absolute; left: 8px; top: 0; width: 8px; height: 18px; background: var(--brand-blue); }
  .video-controls .vol { width: 46px; height: 10px; background: repeating-linear-gradient(90deg, var(--brand-blue) 0 2px, transparent 2px 4px); }
  .video-controls .full { width: 18px; height: 12px; border: 2px solid var(--brand-blue); border-radius: 3px; }

  .hero-intro {
    position: absolute; left: 710px; top: 424px; width: 440px;
    font-family: Oswald, "Arial Narrow", sans-serif; font-weight: 300; font-size: 22px;
    line-height: 26px; color: #333; text-transform: uppercase; letter-spacing: -0.4px;
  }
  .hero-intro strong { color: var(--brand-blue); font-weight: 400; }

  .testimonials { position: absolute; left: 26px; top: 571px; width: 460px; }
  .testimonial { position: relative; height: 165px; padding-left: 111px; }
  .testimonial-photo { position: absolute; left: 0; top: 0; width: 89px; height: 89px; border: 1px solid #999; }
  .testimonial-photo.p-one { background: linear-gradient(135deg, #c9b08a, #4a3b30); }
  .testimonial-photo.p-two { background: linear-gradient(135deg, #7a8a5a, #3d3224); }
  .testimonial p { font-size: 13.8px; line-height: 16.5px; color: var(--body-grey); }
  .testimonial-name { margin-top: 14px; font-family: Oswald, "Arial Narrow", sans-serif; font-weight: 300; font-size: 22px; color: #444; line-height: 24px; }
  .testimonial-place { font-size: 13.5px; color: var(--body-grey); }

  .divider { position: absolute; left: 503px; top: 566px; width: 1px; height: 307px; background: var(--divider); }

  .offer { position: absolute; left: 546px; top: 568px; width: 634px; }
  .btn-start {
    display: inline-block; width: 263px; height: 61px; background: var(--brand-blue);
    border: 2px solid #1d7fb0; outline: 2px solid #9ad6f1; outline-offset: -5px;
    font-family: Oswald, "Arial Narrow", sans-serif; font-weight: 500; font-size: 40px;
    line-height: 56px; color: var(--white); text-align: center; text-transform: uppercase; vertical-align: middle;
  }
  .discount { display: inline-block; margin-left: 28px; vertical-align: middle; font-family: Oswald, "Arial Narrow", sans-serif; font-weight: 300; font-size: 26px; color: #444; }
  .discount em { font-style: normal; color: var(--brand-blue); }
  .offer p { margin-top: 18px; font-size: 16.3px; line-height: 20.5px; color: var(--body-grey); }
  .offer .sign-off { margin-top: 20px; }
  .signature { margin-top: 4px; width: 140px; height: 34px; background: linear-gradient(90deg, rgba(41,168,224,0.55), rgba(41,168,224,0.1)); border-radius: 17px; }

  .footer { position: absolute; left: 0; top: 908px; width: 1200px; height: 164px; background: var(--footer-bg); }
  .footer-links { position: absolute; left: 397px; top: 55px; display: flex; gap: 16px; list-style: none; font-size: 14.5px; color: var(--brand-blue); }
  .copyright { position: absolute; left: 397px; top: 84px; font-size: 13px; color: #ddd; }
</style>
</head>
<body>
  <header class="hero">
    <div class="hero-portrait" role="img" aria-label="Black and white portrait of the vocal coach smiling, in a dark jumper"></div>

    <div class="brand">
      <span class="brand-dot"></span>
      <span class="brand-name">AdrianKell<small>School of Voice</small></span>
    </div>

    <div class="social" aria-label="Social links">
      <span class="s-one"></span><span class="s-two"></span>
    </div>

    <ul class="main-nav">
      <li class="is-active">Home</li>
      <li>Voice Lessons</li>
      <li>Blog</li>
      <li>What Students Say</li>
      <li>The Instructors</li>
      <li>Vocal Ascent</li>
    </ul>

    <div class="video">
      <div class="video-frame" role="img" aria-label="Video still of the vocal coach speaking to camera against a dark backdrop"></div>
      <div class="video-controls">
        <span class="play"></span>
        <span class="time">00:00</span>
        <span class="track"></span>
        <span class="time">04:17</span>
        <span class="vol"></span>
        <span class="full"></span>
      </div>
    </div>

    <p class="hero-intro">Professional vocal coach, <strong>Adrian P. Kell</strong> has laid the vocal foundation for thousands of singers worldwide, for 20+ years.</p>
  </header>

  <section class="testimonials">
    <article class="testimonial">
      <div class="testimonial-photo p-one" role="img" aria-label="Portrait of student Mara Lindqvist"></div>
      <p>I have found through the years that the one method I can count on is Vocal Ascent. Adrian Kell has put together the fool proof method for training a voice that is dependable aand authentic as you grow through your vocal practice.</p>
      <div class="testimonial-name">Mara Lindqvist</div>
      <div class="testimonial-place">San Francisco</div>
    </article>
    <article class="testimonial">
      <div class="testimonial-photo p-two" role="img" aria-label="Portrait of student Declan Forde"></div>
      <p>Since starting the program, my singing progress has been described as phenomenal, 400% improvement. My teachers have worked with people such as Dame Elin Harcourt, and they are impressed with my voice.</p>
      <div class="testimonial-name">Declan Forde</div>
      <div class="testimonial-place">Australia</div>
    </article>
  </section>

  <div class="divider"></div>

  <section class="offer">
    <span class="btn-start">Get Started</span>
    <span class="discount"><em>30% Discount</em> Use Code: VA414</span>
    <p>I believe in Vocal Ascent wholeheartedly, and I want you to be fully satisfied with the program.That’s why I stand behind Vocal Ascent with a 100%&nbsp; money-back guarantee.</p>
    <p>I am confident that by making this small investment now, you will learn the keys to achieving having a breakthrough with your voice.</p>
    <p class="sign-off">Subcerely yours,</p>
    <div class="signature" role="img" aria-label="Handwritten signature of Adrian Kell"></div>
  </section>

  <footer class="footer">
    <div class="brand">
      <span class="brand-dot"></span>
      <span class="brand-name">AdrianKell<small>School of Voice</small></span>
    </div>
    <ul class="footer-links">
      <li>Home</li><li>About us</li><li>Support</li><li>APKMethod</li><li>Privacy Policy</li><li>Terms of use</li><li>Sitemap</li>
    </ul>
    <p class="copyright">© Copyright 2009. APKVoice.com. All Rights Reserved.</p>
    <div class="social" aria-label="Social links">
      <span class="s-one"></span><span class="s-two"></span>
    </div>
  </footer>
</body>
</html>
```